クリニックで使用する封筒(角2、長3の2サイズ)のデザインをお願いします。

【カラーリング】
・別添のロゴマークに使用してある色(グリーン・ブルーや白を基調とした色

【デザイン】
・さりげなくロゴが印象に残る形で

【用途】
(角2)書類の郵送
(長3)同上

※両サイズともデザインを統一して頂ければと思います。
クリニック名(医療法人社団松浦クリニック、医療法人社団は(医)と表記 して可)、郵便番号・住所(158ー0093、東京都豊島区南青葉台4ー7ー3碧山ビル3F、電話番号(03-6281-4370)、ロゴマーク
水色系、緑系

ロゴと字のバランスが良く仕事上で使いやすそうと感じたため選ばせていただきました。

多くのデザインをお寄せいただきありがとうございました。印象にのこるデザイン、目を引くデザインなど多々ありました。今後機会がありましたらぜひよろしくお願いいたします。

```html
<!DOCTYPE html>
<html lang="ja">
<head>
<meta charset="UTF-8">
<title>松浦クリニック 角2封筒</title>
<link href="https://fonts.googleapis.com/css2?family=Noto+Sans+JP:wght@400;500;700&display=swap" rel="stylesheet">
<style>
  :root {
    --backdrop: #d9d9d9;
    --paper: #ffffff;
    --tint: #e6f2d6;
    --brand-green: #7dbb3c;
    --rule-green: #5aa86a;
    --ink: #4a4a4a;
    --ink-soft: #7a7a7a;
    --flap-edge: #cfcfcf;
  }
  * { margin: 0; padding: 0; box-sizing: border-box; }
  html, body {
    width: 805px; height: 1200px; overflow: hidden;
    background: var(--backdrop);
    font-family: "Noto Sans JP", sans-serif;
  }
  .envelope {
    position: absolute; left: 21px; top: 21px;
    width: 763px; height: 1159px;
  }
  .envelope__shape { position: absolute; inset: 0; }
  .sender-logo {
    position: absolute; left: 72px; top: 1048px;
    font-weight: 700; font-size: 34px; letter-spacing: 1px;
    color: var(--brand-green);
    display: flex; align-items: center; gap: 10px;
  }
  .sender-logo__dot {
    width: 14px; height: 14px; border-radius: 50%;
    background: var(--brand-green);
  }
  .sender-info {
    position: absolute; left: 341px; top: 946px; width: 356px;
    color: var(--ink);
  }
  .sender-info__name {
    font-size: 15px; font-weight: 500; letter-spacing: 1px;
    padding-bottom: 8px;
    border-bottom: 2px solid var(--rule-green);
  }
  .sender-info__name .corp { font-size: 11px; margin-right: 10px; }
  .sender-info__name .clinic { font-size: 17px; }
  .sender-info__postal { font-size: 10px; color: var(--ink-soft); margin-top: 12px; }
  .sender-info__address,
  .sender-info__tel {
    font-size: 14px; color: var(--ink-soft); letter-spacing: 1.5px; margin-top: 8px;
  }
</style>
</head>
<body>
  <div class="envelope">
    <svg class="envelope__shape" viewBox="0 0 763 1159" width="763" height="1159">
      <defs>
        <linearGradient id="footerTint" x1="0" y1="0" x2="0" y2="1">
          <stop offset="0.7" stop-color="#ffffff"/>
          <stop offset="1" stop-color="#e3f0d2"/>
        </linearGradient>
      </defs>
      <rect x="0" y="58" width="763" height="1101" fill="url(#footerTint)"/>
      <path d="M0 58 L28 0 L735 0 L763 58 Z" fill="var(--paper)"/>
      <line x1="0" y1="58" x2="763" y2="58" stroke="var(--flap-edge)" stroke-width="1.5"/>
    </svg>

    <div class="sender-logo">
      <span class="sender-logo__dot"></span>
      <span>松浦クリニック</span>
    </div>

    <div class="sender-info">
      <p class="sender-info__name"><span class="corp">医療法人社団</span><span class="clinic">松浦クリニック</span></p>
      <p class="sender-info__postal">〒158ー0093</p>
      <p class="sender-info__address">東京都豊島区南青葉台4ー7ー3碧山ビル3F</p>
      <p class="sender-info__tel">TEL.03-6281-4370</p>
    </div>
  </div>
</body>
</html>
```